Business card design needed

i need a business card designed for my hair salon its call parlour 71 i want the cards to look similar to the velvet 88 design a big 71 with studio written in the top part of the 3.The 71 big on the left side then all my details (number address name) would love it to be a vintage look, colours to be in black and white/silver card to b black.
to have a line on the back with appointment day time, also would love a vip card like the vip drink card but with free treatments or shampoo so five visits that can b stamped and get a free treatment then 10th get 10% off... or something like that...
Industry/Entity Type
Hair
Contact Information for Business Card
Parlour 71
Mira Dunwoody
0431279406
71 Orchard Crescent, Tallow Bend

```html
<!DOCTYPE html>
<html lang="en">
<head>
<meta charset="utf-8">
<title>Parlour 71 – Business &amp; Loyalty Cards</title>
<link rel="stylesheet" href="https://fonts.googleapis.com/css2?family=Didact+Gothic&display=swap">
<style>
  :root {
    --ink: #231f20;
    --paper: #f4f4f2;
    --backdrop: #3b3b3b;
    --rule: #555;
    --card-w: 560px;
    --card-h: 340px;
  }
  * { box-sizing: border-box; margin: 0; padding: 0; }
  html, body {
    width: 1200px; height: 900px; overflow: hidden;
    background: var(--backdrop);
    font-family: "Didact Gothic", "Century Gothic", sans-serif;
  }
  .stage {
    position: relative; width: 1200px; height: 900px;
  }
  .card {
    position: absolute; left: 320px;
    width: var(--card-w); height: var(--card-h);
    overflow: hidden;
    box-shadow: 0 6px 18px rgba(0,0,0,.35);
  }
  .card--loyalty { top: 70px; background: var(--paper); }
  .card--contact { top: 490px; background: var(--ink); }

  /* loyalty card */
  .loyalty__band {
    position: absolute; left: 0; top: 0; bottom: 0; width: 190px;
    background: var(--ink);
    display: flex; align-items: center; justify-content: center;
  }
  .brand-name {
    font-size: 34px; letter-spacing: 1px; line-height: 1.05;
    text-align: center;
  }
  .loyalty__band .brand-name { color: var(--paper); }
  .stamps {
    position: absolute; right: 36px; top: 26px;
    display: grid; grid-template-columns: repeat(5, 38px); gap: 10px 9px;
  }
  .stamp {
    width: 38px; height: 38px; border-radius: 50%;
    border: 2px solid var(--ink);
  }
  .booking {
    position: absolute; left: 222px; right: 40px; bottom: 30px;
    color: var(--ink); font-size: 13px; line-height: 1;
  }
  .booking__row { display: flex; align-items: flex-end; gap: 6px; height: 20px; }
  .booking__label { width: 38px; }
  .booking__line { flex: 1; border-bottom: 1px solid var(--rule); height: 12px; }
  .booking__line--short { flex: 0 0 160px; }
  .booking__days { letter-spacing: 7px; font-size: 12px; padding-bottom: 2px; }
  .booking__row--date { justify-content: flex-start; }

  /* contact card */
  .contact__panel {
    position: absolute; left: 0; top: 0; bottom: 0; width: 215px;
    background: var(--paper);
    display: flex; align-items: center; justify-content: center;
  }
  .contact__panel .brand-name { color: var(--ink); }
  .contact__details {
    position: absolute; left: 240px; right: 20px; top: 120px;
    color: var(--paper); text-align: center;
  }
  .contact__name { font-size: 27px; letter-spacing: 1px; font-weight: 400; }
  .contact__phone { font-size: 15px; letter-spacing: 1px; margin-top: 14px; }
  .contact__address { font-size: 15px; letter-spacing: .5px; margin-top: 4px; }
</style>
</head>
<body>
<main class="stage">

  <section class="card card--loyalty" aria-label="Loyalty and appointment card">
    <div class="loyalty__band">
      <p class="brand-name">Parlour<br>71</p>
    </div>
    <div class="stamps" aria-label="Ten stamp spaces">
      <span class="stamp"></span><span class="stamp"></span><span class="stamp"></span><span class="stamp"></span><span class="stamp"></span>
      <span class="stamp"></span><span class="stamp"></span><span class="stamp"></span><span class="stamp"></span><span class="stamp"></span>
    </div>
    <div class="booking">
      <div class="booking__row"><span class="booking__label">Appt:</span><span class="booking__line"></span></div>
      <div class="booking__row booking__row--date"><span class="booking__label">Date:</span><span class="booking__days">MTWTFS</span><span class="booking__line booking__line--short"></span></div>
      <div class="booking__row"><span class="booking__label">Time:</span><span class="booking__line booking__line--short"></span></div>
    </div>
  </section>

  <section class="card card--contact" aria-label="Business card">
    <div class="contact__panel">
      <p class="brand-name">Parlour<br>71</p>
    </div>
    <div class="contact__details">
      <h1 class="contact__name">Mira Dunwoody</h1>
      <p class="contact__phone">0431279406</p>
      <p class="contact__address">71 Orchard Crescent, Tallow Bend</p>
    </div>
  </section>

</main>
</body>
</html>
```